Architecture firm needing a business card

We need a business card design for a new company based in the US called "Pellmore Architecture". Seeking minimalist designs that have a creativity/design feel but must be clean and professional. Please refer to the logo attached.

Target Market(s)

Real Estate Investors, Home Builders and Construction Firms.

Industry/Entity Type

Architecture

Contact Information for Business Card

Standard US size business cards. Would like to have some sort of graphic on the back side of the card - nothing that is too loud but something that may catch your attention. More or less grayscale colors that are in line with the logo colors (navy and greys essentially). Additional colors maybe accepted if blended properly (earthtones), but might be difficult to accomplish and maintain the clean/minimalist look.

Requirements
Must have
• Clean Lines
Nice to have
• some sort of graphics, would like to have something creative on the back side of the card
Should not have
• nothing too busy, cluttered or overwhelming.

```html
<!DOCTYPE html>
<html lang="en">
<head>
<meta charset="utf-8">
<title>Pellmore Architecture – Business Card</title>
<link rel="stylesheet" href="https://fonts.googleapis.com/css2?family=Jost:wght@400&display=swap">
<style>
  :root {
    --backdrop: #898a8a;
    --navy: #1c3f66;
    --card-white: #e9e9eb;
    --grey-text: #8c8c8e;
    --grey-mark: #9a9a9a;
    --rule: #6d8aa8;
    --white: #ffffff;
  }
  * { margin: 0; padding: 0; box-sizing: border-box; }
  html, body { width: 1200px; height: 900px; overflow: hidden; }
  body {
    background: var(--backdrop);
    font-family: "Jost", "Futura", sans-serif;
    font-weight: 400;
    position: relative;
  }
  .card {
    position: absolute;
    left: 321px;
    width: 507px;
    height: 289px;
  }
  .card-front { top: 119px; background: var(--navy); }
  .card-back { top: 471px; background: var(--card-white); }

  .front-wordmark {
    position: absolute;
    left: 0; right: 0; top: 0; bottom: 0;
    display: flex;
    align-items: center;
    justify-content: center;
    gap: 16px;
    color: var(--white);
    font-size: 25px;
    letter-spacing: 3px;
  }
  .front-wordmark .mark-square {
    width: 30px; height: 30px;
    border: 3px solid var(--white);
  }

  .back-wordmark {
    position: absolute;
    left: 0; right: 0; top: 62px;
    display: flex;
    align-items: center;
    justify-content: center;
    gap: 12px;
    color: var(--navy);
    font-size: 20px;
    letter-spacing: 3px;
  }
  .back-wordmark .mark-square {
    width: 40px; height: 40px;
    border: 4px solid var(--grey-mark);
  }

  .name-row {
    position: absolute;
    left: 29px; right: 27px; top: 176px;
    display: flex;
    align-items: center;
    gap: 2px;
  }
  .name-row .rule { flex: 1; height: 1px; background: var(--rule); }
  .name-row .person { color: var(--navy); font-size: 21px; }
  .name-row .dash { color: var(--navy); font-size: 18px; margin: 0 3px 0 4px; }
  .name-row .role { color: var(--grey-text); font-size: 14px; }

  .contact {
    position: absolute;
    left: 0; right: 0;
    text-align: center;
    color: var(--grey-text);
    font-size: 13px;
  }
  .contact .label { color: var(--navy); margin-right: 2px; }
  .contact .gap { display: inline-block; width: 8px; }
  .address { top: 206px; }
  .phones { top: 231px; font-size: 14px; }
  .online { top: 252px; }
</style>
</head>
<body>
  <section class="card card-front">
    <div class="front-wordmark">
      <span class="mark-square"></span>
      <span class="brand-name">PELLMORE ARCHITECTURE</span>
    </div>
  </section>

  <section class="card card-back">
    <div class="back-wordmark">
      <span class="mark-square"></span>
      <span class="brand-name">PELLMORE</span>
    </div>

    <div class="name-row">
      <span class="rule"></span>
      <span class="person">DANIEL REYES</span>
      <span class="dash">-</span>
      <span class="role">CEO/FOUNDER</span>
      <span class="rule"></span>
    </div>

    <p class="contact address">2140 Larkspur Drive, Boise, Idaho 83702</p>
    <p class="contact phones">
      <span class="label">P :</span> 208 555 0147<span class="gap"></span>
      <span class="label">F :</span> 208 555 0193
    </p>
    <p class="contact online">
      <span class="label">E :</span> daniel@pellmore.com<span class="gap"></span>
      <span class="label">W :</span> www.pellmore.com
    </p>
  </section>
</body>
</html>
```